Bright Quest Appeal needs a brochure

I need an A4 - Two sided brochure design.
It's for a maths challenge fundraiser for primary schools throughout Australia.
It needs to be bright and fun with the pictures / files supplied,
Please use as many pics as you can, more the better...
Also keep Logos as transparent
See our website for an idea of what we do pls. thebrightquest.example
Pls make it FUN ....NOT corporate..
so curves and colours rather than straight lines
The only headings that need to be ALL capitals is "FREE TO JOIN" & "FUNDRAISER" Other titles not all capitals pls
Please note: when putting in the pics of the games, pls put in order from game1-7 as they go in order of the school grade levels (Preschool to Grade 6). showing teachers how they become more difficult...in that order.
This brochure will be sent to schools.
Schools have admin open letters, we get about 2 - 3 seconds for admin to decide to keep or bin the brochure, so they need to see it's a fundraiser and "free to join" in those seconds.
cheers
- fun style maybe marker felt or comic sans but you choose any other you think works to make it fun

```html
<!DOCTYPE html>
<html lang="en">
<head>
<meta charset="utf-8">
<title>Bright Quest Appeal – Maths Challenge Brochure</title>
<link rel="stylesheet" href="https://fonts.googleapis.com/css2?family=Lilita+One&family=Comic+Neue:ital,wght@0,400;0,700;1,400&family=Montserrat:wght@400;500&family=Patrick+Hand&display=swap">
<style>
:root{
  --red:#e31e26;
  --red-dark:#c9151c;
  --ink:#1b1b1b;
  --white:#ffffff;
  --grey-bg:#c8c8c8;
  --page-grey:#cfcfcf;
  --gold:#d9ad3a;
}
*{box-sizing:border-box;margin:0;padding:0}
html,body{width:1200px;height:2549px;overflow:hidden;background:var(--grey-bg)}
body{position:relative;font-family:"Comic Neue",sans-serif;color:var(--ink)}
.spread{position:absolute;left:50px;width:1000px;height:708px;transform:scale(1.1);transform-origin:0 0;box-shadow:0 6px 18px rgba(0,0,0,.35);display:flex}
.spread--outside{top:420px}
.spread--inside{top:1360px}
.page{position:relative;width:500px;height:708px;overflow:hidden}
.page--white{background:var(--white)}
.page--grey{background:linear-gradient(90deg,var(--page-grey) 0%,#f2f2f2 45%,#fafafa 100%)}
.abs{position:absolute}
.svg-layer{position:absolute;left:0;top:0}
.heading{font-family:"Lilita One",sans-serif;font-weight:400}
.heading--red{color:var(--red)}
.heading--white{color:var(--white)}
.body-copy{font-size:12.5px;line-height:1.2}
.games-title{top:22px;left:0;width:500px;text-align:center;font-size:17px}
.game-tile{position:absolute;width:138px;height:104px;border-radius:10px;border:2px solid #111}
.brand-mark{display:flex;align-items:center;gap:8px}
.brand-mark__dot{width:22px;height:22px;border-radius:50%;background:var(--red)}
.brand-mark__name{font-family:"Lilita One",sans-serif;font-size:24px;color:var(--red)}
.promoted{top:516px;left:24px;font-size:13px}
.partner{top:512px;left:128px;display:flex;align-items:center;gap:6px}
.partner__dot{width:20px;height:20px;border-radius:50%;background:var(--white)}
.partner__name{font-family:"Lilita One",sans-serif;font-size:14px;color:var(--white)}
.start-line{top:570px;left:24px;font-size:15px}
.contact{display:flex;align-items:center;gap:10px;color:var(--white);font-size:12.5px;font-family:"Comic Neue",sans-serif;font-weight:700}
.contact--phone{top:602px;left:24px;font-family:"Lilita One",sans-serif;font-weight:400;font-size:18px}
.contact--mail{top:641px;left:24px}
.contact--web{top:641px;left:256px}
.icon-disc{width:24px;height:24px;border-radius:50%;background:var(--white);display:flex;align-items:center;justify-content:center}
.tagline{top:148px;left:0;width:500px;text-align:center;font-family:"Montserrat",sans-serif;font-size:11px}
.title-small{top:172px;left:0;width:500px;text-align:center;font-size:37px;color:var(--ink)}
.title-big{top:212px;left:0;width:500px;text-align:center;font-size:62px;line-height:1;color:var(--red)}
.quote{top:290px;left:0;width:500px;text-align:center;font-style:italic;font-size:19px;line-height:1.15}
.cloud-caption{top:366px;left:170px;width:180px;text-align:center;font-family:"Patrick Hand",cursive;font-size:19px;line-height:1.25;color:var(--ink);transform:rotate(4deg)}
.site-url{top:660px;left:0;width:500px;text-align:center;font-size:17px;letter-spacing:.3px}
.bullets{list-style:none}
.bullets li{position:relative;padding-left:26px;margin-bottom:12px;font-size:12.5px;line-height:1.2}
.bullets li::before{content:"";position:absolute;left:0;top:2px;width:10px;height:10px;border-radius:50%;border:2.5px solid var(--red);background:var(--white)}
.bullets--white li{color:var(--white)}
.bullets--white li::before{border-color:var(--white);background:transparent}
.cert{top:15px;left:287px;width:180px;height:262px;background:#222;padding:8px}
.cert__inner{width:100%;height:100%;background:linear-gradient(160deg,#f6d56b,var(--gold) 50%,#b9851d)}
.pill{top:118px;left:26px;height:28px;padding:0 16px;border-radius:14px;background:var(--ink);color:var(--white);font-size:15px;line-height:28px}
</style>
</head>
<body>

<section class="spread spread--outside">
  <div class="page page--white">
    <h2 class="abs heading games-title">Over 260 maths games for Foundation to Grade 6 !</h2>

    <svg class="svg-layer" width="500" height="708" viewBox="0 0 500 708" aria-hidden="true">
      <g stroke="var(--red)" stroke-width="1.6" fill="none">
        <path d="M103 125 H70 V182"/>
        <path d="M70 285 V352 H103"/>
        <path d="M395 125 H428 V182"/>
        <path d="M428 285 V352 H395"/>
      </g>
      <g fill="var(--ink)">
        <rect x="0" y="478" width="500" height="230"/>
        <circle cx="20" cy="478" r="30"/><circle cx="80" cy="462" r="40"/><circle cx="160" cy="462" r="38"/>
        <circle cx="230" cy="478" r="30"/><circle cx="300" cy="486" r="30"/><circle cx="370" cy="492" r="32"/>
        <circle cx="440" cy="488" r="30"/><circle cx="500" cy="480" r="30"/>
      </g>
      <g fill="var(--red)">
        <rect x="0" y="490" width="500" height="218"/>
        <circle cx="26" cy="490" r="30"/><circle cx="86" cy="474" r="40"/><circle cx="166" cy="474" r="38"/>
        <circle cx="236" cy="490" r="30"/><circle cx="306" cy="498" r="30"/><circle cx="376" cy="504" r="32"/>
        <circle cx="446" cy="500" r="30"/><circle cx="506" cy="492" r="30"/>
      </g>
    </svg>

    <div class="game-tile" style="left:103px;top:66px;background:linear-gradient(135deg,#3a2f8a,#7a3aa0)" role="img" aria-label="Game 1 screenshot: 3D shapes puzzle"></div>
    <div class="game-tile" style="left:257px;top:66px;background:linear-gradient(135deg,#5b86c9,#c98a4a)" role="img" aria-label="Game 2 screenshot: money sorting game"></div>
    <div class="game-tile" style="left:28px;top:182px;background:linear-gradient(135deg,#3aa84a,#e6d23a)" role="img" aria-label="Game 3 screenshot: counting game"></div>
    <div class="game-tile" style="left:181px;top:182px;background:linear-gradient(135deg,#2a5fae,#1d3a70)" role="img" aria-label="Game 4 screenshot: clock reading game"></div>
    <div class="game-tile" style="left:334px;top:182px;background:linear-gradient(135deg,#2f4fb0,#1e3490)" role="img" aria-label="Game 5 screenshot: area of a room game"></div>
    <div class="game-tile" style="left:103px;top:300px;background:linear-gradient(135deg,#1b2440,#0d1224)" role="img" aria-label="Game 6 screenshot: number dials game"></div>
    <div class="game-tile" style="left:257px;top:300px;background:linear-gradient(135deg,#444,#1c1c1c)" role="img" aria-label="Game 7 screenshot: decimals tile game"></div>

    <p class="abs heading heading--white promoted">Promoted by:</p>
    <div class="abs partner"><span class="partner__dot"></span><span class="partner__name">Fundwise Schools</span></div>
    <p class="abs heading heading--white start-line">Start a Maths Challenge for your school:</p>
    <div class="abs contact contact--phone">
      <span class="icon-disc"><svg width="14" height="14" viewBox="0 0 24 24"><path d="M6.6 10.8a15 15 0 0 0 6.6 6.6l2.2-2.2c.3-.3.7-.4 1-.2 1.1.4 2.300.6 3.6.6.6 0 1 .4 1 1V20c0 .6-.4 1-1 1A17 17 0 0 1 3 4c0-.6.4-1 1-1h3.5c.6 0 1 .4 1 1 0 1.3.2 2.5.6 3.6.1.3 0 .7-.2 1z" fill="var(--red)"/></svg></span>
      1300 555 010
    </div>
    <div class="abs contact contact--mail">
      <span class="icon-disc"><svg width="14" height="14" viewBox="0 0 24 24"><rect x="3" y="5" width="18" height="14" rx="1" fill="var(--red)"/><path d="M3 6l9 7 9-7" stroke="#fff" stroke-width="1.6" fill="none"/></svg></span>
      info@thebrightquest.example
    </div>
    <div class="abs contact contact--web">
      <span class="icon-disc"><svg width="14" height="14" viewBox="0 0 24 24" fill="none" stroke="var(--red)" stroke-width="1.8"><circle cx="12" cy="12" r="9"/><path d="M3 12h18M12 3c3 3 3 15 0 18M12 3c-3 3-3 15 0 18"/></svg></span>
      www.thebrightquest.example
    </div>
  </div>

  <div class="page page--grey">
    <svg class="svg-layer" width="500" height="708" viewBox="0 0 500 708" aria-hidden="true">
      <path d="M0 470 C150 440 350 440 500 470 V708 H0 Z" fill="var(--red)"/>
    </svg>
    <div class="abs brand-mark" style="top:56px;left:160px"><span class="brand-mark__dot"></span><span class="brand-mark__name">The Bright Quest</span></div>
    <p class="abs tagline">Fun games developing confidence in mathematics.</p>
    <h1 class="abs heading title-small">Maths Challenge</h1>
    <h1 class="abs heading title-big">FUNDRAISER</h1>
    <p class="abs quote">“A great fundraiser helping primary school<br>students with maths!”</p>

    <svg class="svg-layer" width="500" height="708" viewBox="0 0 500 708" role="img" aria-label="Photo: group of cheering primary school children in a classroom">
      <defs><linearGradient id="kidsPhoto" x1="0" y1="360" x2="0" y2="620" gradientUnits="userSpaceOnUse"><stop offset="0" stop-color="#ffffff"/><stop offset=".3" stop-color="#f1ede6"/><stop offset=".55" stop-color="#b58d74"/><stop offset="1" stop-color="#4f6a8a"/></linearGradient></defs>
      <g fill="var(--ink)">
        <circle cx="250" cy="440" r="90"/><circle cx="150" cy="470" r="70"/><circle cx="360" cy="470" r="75"/>
        <circle cx="70" cy="520" r="50"/><circle cx="430" cy="520" r="50"/><rect x="60" y="480" width="380" height="140" rx="40"/>
      </g>
      <g fill="url(#kidsPhoto)">
        <circle cx="250" cy="444" r="84"/><circle cx="150" cy="474" r="64"/><circle cx="360" cy="474" r="69"/>
        <circle cx="72" cy="522" r="44"/><circle cx="428" cy="522" r="44"/><rect x="66" y="486" width="368" height="128" rx="36"/>
      </g>
    </svg>
    <p class="abs cloud-caption">Bright Quest<br>done!</p>
    <p class="abs heading heading--white site-url">www.thebrightquest.example</p>
  </div>
</section>

<section class="spread spread--inside">
  <div class="page page--white">
    <svg class="svg-layer" width="500" height="708" viewBox="0 0 500 708" aria-hidden="true">
      <path d="M0 455 C120 420 300 400 500 440 V708 H0 Z" fill="var(--ink)"/>
      <path d="M0 470 C120 435 300 415 500 455 V708 H0 Z" fill="var(--red)"/>
    </svg>
    <h3 class="abs heading heading--red" style="top:14px;left:24px;font-size:19px">Students love a challenge !</h3>
    <p class="abs body-copy" style="top:50px;left:24px;width:220px">Students are challenged to solve educational maths games on The Bright Quest website.</p>
    <h3 class="abs heading heading--red" style="top:112px;left:24px;font-size:19px;line-height:1.05;width:230px">It’s lots of fun and helps students with maths !</h3>
    <p class="abs body-copy" style="top:178px;left:24px;width:240px">The maths challenge is designed to build confidence in mathematics for primary school students.</p>
    <p class="abs body-copy" style="top:236px;left:24px;width:240px">Once students have completed their maths challenge, they may download a certificate of congratulations.</p>
    <div class="abs cert"><div class="cert__inner" role="img" aria-label="Gold certificate of congratulations awarded for completing the challenge"></div></div>

    <svg class="svg-layer" width="500" height="708" viewBox="0 0 500 708" role="img" aria-label="Photos: girl cheering on a sofa with a laptop, and two children giving a high five at a laptop">
      <defs>
        <linearGradient id="sofaPhoto" x1="0" y1="310" x2="0" y2="480" gradientUnits="userSpaceOnUse"><stop offset="0" stop-color="#e7e2da"/><stop offset="1" stop-color="#b7a89a"/></linearGradient>
        <linearGradient id="fivePhoto" x1="0" y1="350" x2="0" y2="490" gradientUnits="userSpaceOnUse"><stop offset="0" stop-color="#d9e6f0"/><stop offset="1" stop-color="#8fa7bb"/></linearGradient>
      </defs>
      <g fill="url(#sofaPhoto)">
        <circle cx="125" cy="360" r="55"/><circle cx="195" cy="380" r="50"/><circle cx="70" cy="410" r="45"/>
        <rect x="35" y="370" width="230" height="110" rx="35"/>
      </g>
      <g fill="var(--ink)"><circle cx="375" cy="410" r="72"/><circle cx="300" cy="440" r="50"/><circle cx="450" cy="445" r="45"/></g>
      <g fill="url(#fivePhoto)"><circle cx="375" cy="412" r="66"/><circle cx="300" cy="442" r="44"/><circle cx="450" cy="447" r="39"/></g>
    </svg>

    <h3 class="abs heading heading--white" style="top:496px;left:24px;font-size:19px;line-height:1.25">Free to Join !<br>Effortless to run !</h3>
    <ul class="abs bullets bullets--white" style="top:565px;left:24px;width:460px">
      <li>It’s all set-up online and ready to go. No spending time or effort planning activities or fundraiser days.</li>
      <li>The Bright Quest website is fully safe and secure with no information sharing, no links to other sites and no popup advertising.</li>
      <li>Plus, all Bright Quest games are aligned with the Australian Mathematics Curriculum.</li>
    </ul>
  </div>

  <div class="page page--grey">
    <h3 class="abs heading heading--red" style="top:28px;left:26px;font-size:19px;line-height:1.55">All set up online for you !<br>Builds confidence in maths for students !<br>Easy to run !</h3>
    <p class="abs heading pill">Here is how it works:</p>
    <ul class="abs bullets" style="top:168px;left:26px;width:420px">
      <li>Let us know how many memberships you need for your Bright Quest Appeal.</li>
      <li>We will send you our website access code for those memberships.</li>
      <li>Download our fundraising letter, photocopy and give to parents to collect funds. (See our website for more details.)</li>
      <li>On the website, each year level has a set of maths challenges for students to solve.</li>
      <li>Once completed students may download a certificate of congratulations.</li>
    </ul>
    <svg class="svg-layer" width="500" height="708" viewBox="0 0 500 708" role="img" aria-label="Photo: smiling students working at computers in a classroom">
      <defs><linearGradient id="labPhoto" x1="0" y1="0" x2="1" y2="1"><stop offset="0" stop-color="#6c6a6a"/><stop offset=".5" stop-color="#c79a7c"/><stop offset="1" stop-color="#3a3a3e"/></linearGradient></defs>
      <path d="M0 420 C150 395 330 395 500 470 V708 H0 Z" fill="var(--red)"/>
      <path d="M0 432 C150 408 330 410 500 484 V708 H0 Z" fill="url(#labPhoto)"/>
    </svg>
  </div>
</section>

</body>
</html>
```